FernlowCo - Business Card and Letterhead

After having received some fantastic submissions in our recent logo design project, I would now like to extend our branding to letterheads and business cards.
FernlowCo is a consulting service in the Construction Industry. We deal with both residential and commercial projects, and our clients include Architects, Builders, Tradespeople and Home Owners.
The designs should be simple and effective, convey personal service and professionalism, and display some level of creativity.
For both the business cards and letterhead, a white card stock will be used. This project is for business cards and letterheads only. Our new logo is attached for use.
The designs should incorporate our two main colours which are Blue (RGB 14,92,143) and Green (RGB 132,194,37).
For the time being, please submit all designs showing generic information including name, mobile number, email, postal address and website details. No fax number or physical address is required. I will provide our actual contact details once a final design has been selected.
I encourage you to interpret this brief in your own creative way, and look forward to some quality submissions.
Thanks!
Leo
FernlowCo.

```html
<!DOCTYPE html>
<html lang="en">
<head>
<meta charset="utf-8">
<title>FernlowCo Business Card</title>
<link rel="stylesheet" href="https://fonts.googleapis.com/css2?family=Arimo:wght@700&family=Questrial&family=Archivo+Narrow:wght@700&display=swap">
<style>
  :root {
    --brand-blue: #0e5c8f;
    --brand-blue-deep: #0a3d66;
    --brand-green: #84c225;
    --ink: #3f3f3f;
    --name-ink: #555555;
    --card-white: #fbfbfb;
    --backdrop: #505050;
  }
  * { margin: 0; padding: 0; box-sizing: border-box; }
  html, body {
    width: 1200px;
    height: 1000px;
    overflow: hidden;
    background: var(--backdrop);
  }
  .canvas {
    position: relative;
    width: 1200px;
    height: 1000px;
  }
  .card {
    position: absolute;
    width: 529px;
    height: 302px;
    border-radius: 14px;
    overflow: hidden;
    box-shadow: 0 3px 8px rgba(0,0,0,0.35);
  }
  .card-front {
    left: 181px;
    top: 170px;
    background: var(--card-white);
  }
  .card-back {
    left: 474px;
    top: 550px;
    background: linear-gradient(180deg, #0f4a7c 0%, var(--brand-blue-deep) 100%);
  }
  .brand {
    position: absolute;
    display: flex;
    align-items: center;
    gap: 9px;
  }
  .brand-mark {
    width: 30px;
    height: 30px;
    background: var(--brand-green);
  }
  .brand-name {
    font-family: "Arimo", Arial, sans-serif;
    font-weight: 700;
    font-size: 36px;
    letter-spacing: -0.3px;
    line-height: 1;
  }
  .card-front .brand { left: 29px; top: 61px; }
  .card-front .brand-name { color: var(--brand-blue); }
  .card-back .brand { left: 119px; top: 133px; }
  .card-back .brand-name { color: #ffffff; }
  .contact {
    position: absolute;
    left: 28px;
    top: 221px;
    font-family: "Questrial", "Century Gothic", sans-serif;
    font-size: 13px;
    line-height: 16.5px;
    color: var(--ink);
  }
  .contact .label {
    font-weight: 700;
    color: var(--brand-blue);
    font-family: "Arimo", Arial, sans-serif;
    font-size: 12px;
  }
  .person-name {
    position: absolute;
    left: 350px;
    top: 221px;
    font-family: "Archivo Narrow", "Arial Narrow", sans-serif;
    font-weight: 700;
    font-size: 23px;
    letter-spacing: 0.4px;
    color: var(--name-ink);
  }
  .accent-band {
    position: absolute;
    left: 0;
    bottom: 0;
    width: 529px;
    height: 17px;
  }
</style>
</head>
<body>
  <main class="canvas">
    <section class="card card-front">
      <div class="brand">
        <span class="brand-mark"></span>
        <span class="brand-name">FernlowCo</span>
      </div>
      <address class="contact" style="font-style:normal">
        27 Harbour Road, Kincumber NSW 2251<br>
        <span class="label">M:</span> 0400 123 456&nbsp;&nbsp;<span class="label">E:</span> hale@fernlowco.com<br>
        www.fernlowco.com
      </address>
      <p class="person-name">MARTIN HALE</p>
      <svg class="accent-band" viewBox="0 0 529 17" aria-hidden="true">
        <polygon points="0,2 327,2 315,15 0,15" fill="var(--brand-blue)"/>
        <polygon points="340,0 529,0 529,17 323,17" fill="var(--brand-green)"/>
      </svg>
    </section>

    <section class="card card-back">
      <div class="brand">
        <span class="brand-mark"></span>
        <span class="brand-name">FernlowCo</span>
      </div>
    </section>
  </main>
</body>
</html>
```